Cardiology Practice needs a Heart Scan Order Form

Busy cardiology practice needs an order form for a heart scan test. Sample is attached. One side should have all information noted and the other side should have our physician names (Vikram Joshi, MD, K.L. Morvandi, MD, Anjali Desai, MD, Parvin Joshi, MD, and Gerald Montefino, MD. It should have the map that is uploaded and our demographic information (Crestline Cardio PLLC, 218 Juniper Ave. Ste. B, Webster, TX 77412 along with phone 713-642-1187 and fax 713-642-1188) as well as our web address (crestlinecardio.example). Our primary colors are red, black and white. Needs to fit paper size 8 1/2 by 11.

Target Market(s)

Healthcare

Industry/Entity Type

Health Care

Font styles to use
Serif

Colors
ec1f27

Requirements
Must have
• Logo, information listed on sample form, demographics and physician names as well as website.
Nice to have
• Open to suggestions
Should not have
• Physician Pictures

```html
<!DOCTYPE html>
<html lang="en">
<head>
<meta charset="utf-8">
<title>Crestline Cardio – Calcium Score Heart Scan Order Form</title>
<link rel="stylesheet" href="https://fonts.googleapis.com/css2?family=Merriweather:wght@700;900&family=Source+Serif+4:wght@400;600;700&display=swap">
<style>
:root{
  --red:#c0323a;
  --ink:#1f1f1f;
  --grey-bg:#6b6b6b;
  --cell-head:#e2e2e2;
  --rule:#8c8c8c;
  --paper:#ffffff;
  --card:#262626;
}
*{box-sizing:border-box;margin:0;padding:0}
html,body{width:1200px;height:1200px;overflow:hidden}
body{background:var(--grey-bg);font-family:"Source Serif 4",serif;color:var(--ink);position:relative}
.sheet{position:absolute;top:233px;width:552px;height:714px;background:var(--paper);overflow:hidden}
.sheet--form{left:32px}
.sheet--team{left:609px}
.abs{position:absolute}

/* brand */
.brand{left:25px;top:34px;width:170px}
.brand__name{font-weight:700;color:var(--red);font-size:13px;letter-spacing:1px;line-height:1;display:flex;align-items:center;gap:5px;white-space:nowrap}
.brand__dot{width:9px;height:9px;border-radius:50%;background:var(--red);display:inline-block;flex:none}
.brand__tag{font-size:6.5px;color:#444;margin-top:5px;padding-left:14px;white-space:nowrap}
.doc-title{left:200px;top:20px;font-family:"Merriweather",serif;font-weight:900;font-size:18px;line-height:26px;color:#2a2a2a;white-space:nowrap}

/* tables */
.tbl{border:1px solid var(--rule);font-size:7.4px}
.tbl__head{background:var(--cell-head);text-align:center;font-weight:600;border-bottom:1px solid var(--rule);height:13px;line-height:13px}
.tbl__row{display:flex;border-bottom:1px solid var(--rule);height:13px;line-height:13px}
.tbl__row:last-child{border-bottom:0}
.tbl__row span{padding-left:3px}
.tbl__label{border-right:1px solid var(--rule);width:42px;font-weight:600;white-space:nowrap}
.schedule{left:389px;top:26px;width:137px}

.names-bar{left:25px;top:91px;width:500px;height:22px;background:var(--red);color:#fff;font-weight:700;font-size:8.8px;display:flex;align-items:center;justify-content:space-between;padding:0 8px;white-space:nowrap}

.field-group{font-size:7.4px}
.patient{left:25px;top:123px;width:237px;height:42px}
.contact{left:288px;top:123px;width:237px;height:42px}
.split{display:flex;height:14px;border-bottom:1px solid var(--rule)}
.split div{border-right:1px solid var(--rule);text-align:center;line-height:13px}
.split div:last-child{border-right:0}
.split--empty{height:13px;border-bottom:0}
.addr{display:flex;height:27px}
.addr div:first-child{width:62px;border-right:1px solid var(--rule);line-height:27px;padding-left:10px}

.mini{top:175px;width:115px;height:28px}
.mini .tbl__head{height:14px;line-height:14px}
.medical-bar{left:25px;top:220px;width:500px;height:18px;background:var(--cell-head);text-align:center;font-weight:700;font-size:9px;line-height:18px}
.inline-field{top:252px;height:14px;display:flex;border:1px solid var(--rule);font-size:7.4px;line-height:12px}
.inline-field span{border-right:1px solid var(--rule);padding:0 5px;background:var(--cell-head);font-weight:600}
.inline-field span.opt{background:none;font-weight:400;flex:1;text-align:center}
.inline-field span:last-child{border-right:0}

.diagnosis{left:25px;top:284px;width:500px;font-size:8px;font-weight:600;display:flex;gap:4px;align-items:flex-end}
.diagnosis i{flex:1;border-bottom:1px solid #444;height:9px}
.check-row{left:25px;width:500px;font-size:7.4px;display:flex;align-items:center;white-space:nowrap}
.check-row .c{display:flex;align-items:center;gap:5px}
.box{width:6.5px;height:6.5px;border:1px solid #333;display:inline-block;flex:none}
.blank{display:inline-block;border-bottom:1px solid #444;width:44px;height:7px}

.divider{left:25px;top:403px;width:500px;border-top:1px solid #999}
.notice{left:25px;top:411px;width:500px;font-size:7.8px;font-weight:700;white-space:nowrap}
.instructions{left:25px;top:432px;width:500px;list-style:none;font-size:7.4px;line-height:10px}
.instructions li{display:flex;gap:6px;margin-bottom:4.3px}
.instructions li::before{content:"";flex:none;width:5px;height:5px;border:1px solid #333;margin-top:2.5px}
.ack{left:25px;top:570px;width:500px;font-size:7.4px;line-height:10px}
.sig{width:111px;border-top:1px solid #555;font-size:7.4px;font-weight:600;text-align:center;padding-top:3px;white-space:nowrap}
.referring{left:289px;top:606px;width:237px}
.referring .tbl__row{height:14.5px;line-height:14.5px}
.referring .tbl__label{width:48px}

.footer{left:0;top:672px;width:552px;height:42px;background:var(--red);color:#fff;font-size:8px;line-height:11px;text-align:center;padding-top:9px}
.footer--team{display:flex;align-items:center;justify-content:space-between;padding:0 22px;font-size:8.6px;text-align:left;white-space:nowrap}
.footer--team .item{display:flex;align-items:center;gap:5px}
.footer--team svg{width:10px;height:10px;flex:none}

/* team */
.team-head{left:26px;top:26px;width:500px;height:32px;background:var(--red);color:#fff;font-family:"Merriweather",serif;font-weight:900;font-size:17px;text-align:center;line-height:32px}
.card{width:160px;height:150px;background:var(--card);color:#fff;text-align:center;display:flex;flex-direction:column;justify-content:center;align-items:center;border-top:4px solid var(--red)}
.card__name{font-family:"Merriweather",serif;font-weight:700;font-size:11.5px;line-height:15px;white-space:nowrap}
.card__rule{width:28px;border-top:1px solid var(--red);margin:9px 0}
.card__role{font-size:9px;line-height:11px;color:#eaeaea}
.map{left:26px;top:395px;width:500px;height:266px;border:1px solid #bbb;background:linear-gradient(135deg,#ecebe6 0%,#e4e3de 50%,#efeadc 100%)}
</style>
</head>
<body>

<section class="sheet sheet--form">
  <div class="abs brand">
    <div class="brand__name"><span class="brand__dot"></span>CRESTLINE CARDIO</div>
    <div class="brand__tag">Cardiovascular Center of Excellence</div>
  </div>
  <h1 class="abs doc-title">CALCIUM SCORE<br>HEART SCAN</h1>

  <div class="abs tbl schedule">
    <div class="tbl__head">Test schedule</div>
    <div class="tbl__row"><span class="tbl__label">Test date:</span></div>
    <div class="tbl__row"><span class="tbl__label">Test time:</span></div>
  </div>

  <div class="abs names-bar">
    <span>Vikram Joshi, M.D.</span><span>K.L. Morvandi, M.D.</span><span>Anjali Desai, M.D.</span><span>Parvin Joshi, M.D.</span><span>Gerald Montefino, M.D.</span>
  </div>

  <div class="abs tbl field-group patient">
    <div class="tbl__head">Patient information</div>
    <div class="split"><div style="width:62px">Last name</div><div style="width:106px">First name</div><div style="flex:1">MI</div></div>
    <div class="split split--empty"><div style="width:62px"></div><div style="width:106px"></div><div style="flex:1"></div></div>
  </div>
  <div class="abs tbl field-group contact">
    <div class="tbl__head">Contact information</div>
    <div class="addr"><div>Address:</div><div></div></div>
  </div>

  <div class="abs tbl mini" style="left:25px"><div class="tbl__head">Date of birth</div></div>
  <div class="abs tbl mini" style="left:147px"><div class="tbl__head">Account no.</div></div>
  <div class="abs tbl mini" style="left:288px"><div class="tbl__head">Home phone no.</div></div>
  <div class="abs tbl mini" style="left:410px"><div class="tbl__head">Mobile phone no.</div></div>

  <div class="abs medical-bar">Medical information</div>
  <div class="abs inline-field" style="left:25px;width:115px"><span>Sex:</span><span class="opt">F</span><span class="opt">M</span></div>
  <div class="abs inline-field" style="left:147px;width:115px"><span>Height:</span></div>
  <div class="abs inline-field" style="left:288px;width:115px"><span>Weight:</span></div>
  <div class="abs inline-field" style="left:410px;width:115px"><span style="padding:0 10px">Race:</span></div>

  <div class="abs diagnosis">Diagnosis:<i></i></div>

  <div class="abs check-row" style="top:320px;justify-content:space-between">
    <span class="c"><i class="box"></i>PCI (no. of stents: <i class="blank"></i>)</span>
    <span class="c"><i class="box"></i>CABG (no. of vessels: <i class="blank"></i>)</span>
    <span class="c"><i class="box"></i>MI (last event: <i class="blank"></i>)</span>
    <span class="c"><i class="box"></i>PCM/ICD</span>
  </div>
  <div class="abs check-row" style="top:348px">
    <span class="c" style="width:92px"><i class="box"></i>Diabetes</span>
    <span class="c" style="width:116px"><i class="box"></i>Claustrophobia</span>
    <span class="c" style="width:91px"><i class="box"></i>Asthma</span>
    <span class="c" style="width:109px"><i class="box"></i>Emphysema</span>
    <span class="c"><i class="box"></i>COPD</span>
  </div>
  <div class="abs check-row" style="top:373px">
    <span class="c" style="width:113px">LMP: <i class="blank" style="width:82px"></i></span>
    <span class="c" style="width:70px"><i class="box"></i>bHCG</span>
    <span class="c" style="width:95px"><i class="box"></i>Tubal ligation</span>
    <span class="c" style="width:130px"><i class="box"></i>Post-menopause &gt; 1 year</span>
    <span class="c"><i class="box"></i>Hysterectomy</span>
  </div>

  <div class="abs divider"></div>
  <p class="abs notice">Please read the following instructions carefully. You might be rescheduled if any of the following instructions are not met.</p>
  <ul class="abs instructions">
    <li>AVOID caffeine containing products (coffee, tea, soda, chocolate, energy drinks, or some over the counter medications) for 4 hours prior to testing.</li>
    <li>AVOID smoking for 4 hours prior to testing.</li>
    <li>AVOID eating or drinking anything except water for 4 hours prior to testing.</li>
    <li>Arrive 15 minutes early for your appointment time.</li>
    <li>Wear comfortable clothing. Remove any metal objects, such as jewelry or piercings. Women will be asked to remove bras containing metal underwire.</li>
    <li>Inform your physician or the staff if you are claustrophobic or have a problem staying in restricted environments for any length of time.</li>
    <li>Inform the physician or the staff if you are or think you might be pregnant.</li>
  </ul>
  <p class="abs ack">I hereby acknowledge that the instructions and procedures pertinent to this study were explained thoroughly, I had time to ask questions, and these questions were addressed satisfactorily.</p>

  <div class="abs sig" style="left:26px;top:622px">Patient's print name</div>
  <div class="abs sig" style="left:151px;top:622px">Patient's signature</div>
  <div class="abs sig" style="left:26px;top:655px">Prescriber's print name</div>
  <div class="abs sig" style="left:151px;top:655px">Prescriber's signature</div>

  <div class="abs tbl referring">
    <div class="tbl__head">Referring physician contact information</div>
    <div class="tbl__row"><span class="tbl__label">Order date :</span></div>
    <div class="tbl__row"><span class="tbl__label">Tel no. :</span></div>
    <div class="tbl__row"><span class="tbl__label">Fax no. :</span></div>
  </div>

  <footer class="abs footer">Crestline Cardio, PLLC. Visit us at 218 Juniper Ave. Ste. B, Webster, TX 77412. For appointments or more information on testing,<br>please call (713) 642 1187, or visit www.crestlinecardio.example.</footer>
</section>

<section class="sheet sheet--team">
  <h2 class="abs team-head">OUR PHYSICIAN NAMES</h2>

  <div class="abs card" style="left:26px;top:67px"><div class="card__name">Vikram Joshi, MD</div><i class="card__rule"></i><div class="card__role">Cardiovascular Medicine</div></div>
  <div class="abs card" style="left:196px;top:67px"><div class="card__name">K.L. Morvandi, MD</div><i class="card__rule"></i><div class="card__role">Cardiovascular Medicine</div></div>
  <div class="abs card" style="left:366px;top:67px"><div class="card__name">Anjali Desai, MD</div><i class="card__rule"></i><div class="card__role">Cardiovascular Medicine</div></div>
  <div class="abs card" style="left:111px;top:228px"><div class="card__name">Parvin Joshi, MD</div><i class="card__rule"></i><div class="card__role">Cardiovascular Disease</div></div>
  <div class="abs card" style="left:281px;top:228px"><div class="card__name">Gerald Montefino, MD</div><i class="card__rule"></i><div class="card__role">Cardiovascular Disease</div></div>

  <div class="abs map" role="img" aria-label="Street map showing the Crestline Cardio office location in Webster, TX"></div>

  <footer class="abs footer footer--team">
    <span class="item"><svg viewBox="0 0 10 10"><path d="M5 9.5C2.8 6.8 1.8 5.2 1.8 3.8a3.2 3.2 0 0 1 6.4 0c0 1.4-1 3-3.2 5.7z" fill="none" stroke="#fff" stroke-width="0.9"/><circle cx="5" cy="3.8" r="1.1" fill="none" stroke="#fff" stroke-width="0.8"/></svg>218 Juniper, Suite B, Webster, TX</span>
    <span class="item"><svg viewBox="0 0 10 10"><path d="M2.2 1h1.7l.8 2-1.1.8a5.5 5.5 0 0 0 2.6 2.6l.8-1.1 2 .8v1.7c0 .6-.5 1.200-1.2 1.1C4.4 8.6 1.4 5.6 1.1 2.2 1 1.5 1.6 1 2.2 1z" fill="none" stroke="#fff" stroke-width="0.9"/></svg>713-642-1187</span>
    <span class="item"><svg viewBox="0 0 10 10"><rect x="1" y="3.5" width="8" height="5.5" fill="none" stroke="#fff" stroke-width="0.9"/><rect x="2.8" y="1" width="4.4" height="2.5" fill="none" stroke="#fff" stroke-width="0.9"/><path d="M3 5.5h1M5 5.5h1M3 7h1M5 7h1" stroke="#fff" stroke-width="0.8"/></svg>713-642-1188</span>
    <span class="item"><svg viewBox="0 0 10 10"><circle cx="5" cy="5" r="4" fill="none" stroke="#fff" stroke-width="0.9"/><ellipse cx="5" cy="5" rx="1.8" ry="4" fill="none" stroke="#fff" stroke-width="0.8"/><path d="M1 5h8" stroke="#fff" stroke-width="0.8"/></svg>www.crestlinecardio.example</span>
  </footer>
</section>

</body>
</html>
```